Postcard Design

We are Brightmoor Care. A new way of providing quality healthcare for less. We offer a monthly membership program for $77 per person, $167 per family and cover about 85% of medical conditions. Medical office visits are just $7 each. This innovative program have already saved millions of dollars for it's members in health care costs. We are inviting people to a brief, educational meeting to learn more about how they can save money on their healthcare. We need something catchy and upbeat, positive with 1-2 photos inviting them to come find out more. We will be having appetizers. The date is Wednesday, Feb. 18 drop by between 6-8 pm
Industry/Entity Type
Healthcare

```html
<!DOCTYPE html>
<html lang="en">
<head>
<meta charset="utf-8">
<title>Brightmoor Care – Postcard</title>
<link rel="stylesheet" href="https://fonts.googleapis.com/css2?family=Lato:ital,wght@0,400;0,700;0,900;1,400;1,700&family=Jost:wght@400;600&display=swap">
<style>
  :root {
    --orange: #f7973b;
    --peach: #fcd3a8;
    --blue: #0a87b4;
    --sky: #a9c5dc;
    --photo-warm: #ecd9c4;
    --photo-cool: #c9dcea;
    --ink: #1d1d1f;
    --white: #ffffff;
  }
  * { margin: 0; padding: 0; box-sizing: border-box; }
  html, body { width: 1200px; height: 930px; overflow: hidden; background: var(--white); }
  .postcard {
    position: relative;
    width: 1200px;
    height: 930px;
    overflow: hidden;
    font-family: "Lato", sans-serif;
    color: var(--ink);
    background: var(--white);
  }
  .shapes { position: absolute; inset: 0; }
  .intro {
    position: absolute;
    left: 103px;
    top: 60px;
    font-style: italic;
    font-size: 20.5px;
    letter-spacing: 0.35px;
    line-height: 1.25;
    white-space: nowrap;
  }
  .intro p { margin-bottom: 22px; }
  .intro .accent { color: var(--orange); }
  .intro .accent-large { color: var(--orange); font-size: 25px; }
  .invite-title {
    position: absolute;
    left: 185px;
    top: 258px;
    font-family: "Jost", sans-serif;
    font-size: 48px;
    font-weight: 400;
    letter-spacing: 0.5px;
    white-space: nowrap;
  }
  .invite-text {
    position: absolute;
    left: 281px;
    top: 316px;
    font-size: 19px;
    letter-spacing: 0.2px;
    line-height: 1.4;
    white-space: nowrap;
  }
  .event-date {
    position: absolute;
    left: 281px;
    top: 400px;
    font-size: 26px;
    font-weight: 900;
    line-height: 1.3;
    white-space: nowrap;
  }
  .brand {
    position: absolute;
    left: 868px;
    top: 150px;
    width: 300px;
    color: var(--blue);
    font-weight: 700;
    font-size: 58px;
    line-height: 1;
  }
  .contact {
    position: absolute;
    left: 908px;
    top: 326px;
    width: 190px;
    font-size: 19.5px;
    line-height: 1.5;
  }
  .contact span { display: flex; justify-content: space-between; white-space: nowrap; }
  .membership {
    position: absolute;
    left: 100px;
    top: 520px;
    width: 230px;
    text-align: center;
    transform: rotate(-13deg);
    font-family: "Jost", sans-serif;
  }
  .membership h2 {
    font-size: 22px;
    font-weight: 600;
    letter-spacing: 1.5px;
    line-height: 1.15;
    text-transform: uppercase;
  }
  .membership .price {
    margin-top: 22px;
    font-size: 27px;
    font-weight: 400;
    line-height: 1.2;
  }
  .tagline {
    position: absolute;
    left: 268px;
    top: 830px;
    width: 932px;
    height: 100px;
    padding-left: 104px;
    display: flex;
    align-items: center;
    color: var(--white);
    font-style: italic;
    font-size: 42px;
    letter-spacing: 0.3px;
    white-space: nowrap;
  }
  .tagline strong { font-weight: 700; }
</style>
</head>
<body>
<main class="postcard">
  <svg class="shapes" width="1200" height="930" viewBox="0 0 1200 930">
    <circle class="peach-arc" cx="1010" cy="640" r="350" fill="none" stroke="var(--peach)" stroke-width="40"/>
    <circle class="sky-disc" cx="1045" cy="728" r="333" fill="var(--sky)"/>
    <circle class="peach-dot" cx="692" cy="300" r="76" fill="var(--peach)"/>
    <rect class="side-band" x="0" y="0" width="268" height="930" fill="var(--orange)"/>
    <rect class="tagline-band" x="268" y="830" width="932" height="100" fill="var(--blue)"/>
    <circle class="brand-dot" cx="1020" cy="110" r="26" fill="var(--blue)"/>
    <circle class="badge-ring" cx="197" cy="610" r="152" fill="var(--blue)"/>
    <circle class="badge-face" cx="214" cy="604" r="126" fill="var(--white)"/>
    <circle class="photo-ring" cx="527" cy="733" r="142" fill="var(--orange)"/>
    <circle role="img" aria-label="Photo: smiling family of four with heads together" cx="528" cy="745" r="102" fill="var(--photo-warm)"/>
    <circle class="photo-ring" cx="814" cy="617" r="123" fill="var(--orange)"/>
    <circle role="img" aria-label="Photo: parents walking hand in hand with a toddler outdoors" cx="822" cy="617" r="112" fill="var(--photo-cool)"/>
  </svg>

  <section class="intro">
    <p>We are Brightmoor Care. A new way of providing <span class="accent-large">quality healthcare for less</span>.</p>
    <p>Medical office visits are just <span class="accent">$7</span> each and we cover about 85% of medical conditions.</p>
    <p>This innovative program have already saved millions of dollars<br>for its members in health care costs.</p>
  </section>

  <h1 class="invite-title">our invitation to you....</h1>
  <p class="invite-text">to a brief, educational meeting to learn more about<br>how you can save money on your healthcare.</p>
  <p class="event-date">WEDNESDAY 18 FEBRUARY<br>drop by between 6-8 pm</p>

  <div class="brand">Brightmoor<br>Care</div>
  <p class="contact"><span><b style="font-weight:400">address</b><b style="font-weight:400">telephone</b></span><span><b style="font-weight:400">web address</b><b style="font-weight:400">email</b></span></p>

  <div class="membership">
    <h2>Monthly<br>Memberships</h2>
    <p class="price">$77 per person<br>$167 per family</p>
  </div>

  <p class="tagline">“<strong>Quality</strong>&nbsp;healthcare for the whole family”</p>
</main>
</body>
</html>
```